A label and anti-label for wine.

Hello! How are you? Hope you're good !
We are a vineyard and winery based in Albania with the name Kantina e Drenit. We produce red, white and rose wines.We would like to design a modern label for red, white and rose wine.For this reason, I am addressing you because I have a lot of faith for a very high-quality work.I want the label to include the logo that I sent you in pdf format.You can change the placement of the logo, but without changing the originality or how to make it better and more suitable.
The writing for each label will be:
1. Shiraz 2020 , Alc 14.3%,Vol 0.75l, WINE OF ALBANIA,NATURAL WINE.
info:Rrush Shiraz (Syrah) 100% I vjele gjate datave 20-25 shtator. Vera eshte vjetruar rreth 1 vit ne fuci lisi Kosove. Vera eshte ambalazhuar ne janar 2022 ne rreth 2500 shishe. Vera ruan karakteristikat natyrale te varietetit te rrushit dhe teritorit pasi ka nderhyrje minimale gjate proceve te prodhimit te tij.
Permban doze minimale sulfitesh.
Karakteristikat: ngjyre e kuqe ultraviolet, e thate me tanina te buta, si dhe me acide te moderuara. VeraShiraz 2020 dallon per nje shije te gjate dhe te thekur, qe afron gradualisht me shijen e kumbulles dhecait te malit.
Kjo vere, e ruajtur ne kushte te pershtatshme, mund te arrije cilesite maksimale per gjate viteve 2025-
2028.
2.Riesling 2022 Alc 14.3%,Vol 0.75l, WINE OF ALBANIA,NATURAL WINE.
info:Prodhimi i veres: Rrush Riesling 100% i vjele ne date 20 shtator 2020. Vera eshte stazhonuar per rreth 6 muaj ne kazane inoksi dhe eshte ambalazhuar ne 7 qershor 2022 ne rreth 600 shishe. Vera Riesling nuk ngjashmeri te dukshme me veren e famshme Riesling te gjermanise pasi zhvillon karakteristika te
vecanta teritorit, duke krijuar nje identitet te vecante te veres Riesling.
Karakteristikat: ngjyre limoni, me aroma te theksuar lulesh dhe vecanerisht jasemina, duke zhvilluar gradualisht pas 10-15 minutave shijet e frutave, ku dallohen vecanaerisht ajo e molles dhe pjeshkes.
Kjo vere, e ruajtur ne kushte te pershtatshme, mund te ruaje cilesite maksimale edhe gjate viteve 2023-2024.
3.ROSE 2022 Alc 13%,Vol 0.75l, WINE OF ALBANIA,NATURAL WINE.
info: I will send it next.....
Thank you !

Target Market(s)

Local and foreign market

Industry/Entity Type

Vineyard and winery.

Font styles to use
Sans Serif
Script
Other font styles liked:
• Elegant writing

Colors
0094D4
00A9DD
6FCCEA
C7EBF8
E9F6FB
00AB8E
00BBA5
67D7C9
C6EFE9
E9F9F6
59FF00
82FF00
B8FF75
E3FFCB
F4FFEA
E54698
E96AAD
F1A4CE
F9D9EA
FCEFF6

Requirements
Must have
• There must be a separate design for the label and against the label.
Nice to have
• To make you stand out.
Should not have
• Not be an old model.

```html
<!DOCTYPE html>
<html lang="en">
<head>
<meta charset="utf-8">
<title>Kantina e Drenit – Wine Labels</title>
<link rel="stylesheet" href="https://fonts.googleapis.com/css2?family=Tenor+Sans&family=Josefin+Sans:wght@300;400&family=Roboto+Condensed:wght@300&display=swap">
<style>
  :root {
    --page: #ffffff;
    --paper: #ffffff;
    --riesling: #b4942f;
    --riesling-soft: #c9ad55;
    --rose: #e3579f;
    --rose-soft: #ec7bb6;
    --shiraz-green: #5f7440;
    --shiraz-gold: #c99a3e;
    --shiraz-gold-light: #e2bb68;
    --ink: #4a4a4a;
    --white: #ffffff;
  }
  * { box-sizing: border-box; margin: 0; padding: 0; }
  html, body { width: 1200px; height: 960px; overflow: hidden; background: var(--page); }
  .lineup { position: relative; width: 1200px; height: 960px; }

  .label { position: absolute; width: 320px; overflow: hidden; }
  .label--riesling { left: 100px; top: 380px; height: 450px; --accent: var(--riesling); --accent-soft: var(--riesling-soft); }
  .label--rose { left: 440px; top: 380px; height: 450px; --accent: var(--rose); --accent-soft: var(--rose-soft); }
  .label--shiraz { left: 780px; top: 180px; height: 650px; background: var(--shiraz-gold); }

  .ridge { position: absolute; left: 0; width: 100%; }
  .label--riesling .ridge, .label--rose .ridge {
    top: 12px; height: 124px; background: var(--accent); border-radius: 60px 90px 0 0;
  }
  .paper { position: absolute; left: 0; top: 134px; width: 100%; bottom: 0; background: var(--paper); }

  .title {
    position: absolute; left: 0; width: 100%; text-align: center; white-space: nowrap;
    font-family: "Tenor Sans", sans-serif; font-weight: 400; color: var(--white); line-height: 1;
  }
  .label--riesling .title, .label--rose .title { top: 84px; font-size: 56px; letter-spacing: -1px; }

  .stripe { position: absolute; left: 0; width: 100%; height: 8px; border-top: 2px solid var(--accent); border-bottom: 2px solid var(--accent); }
  .band { position: absolute; left: 0; width: 100%; background: var(--accent); }
  .band-text {
    position: absolute; font-family: "Roboto Condensed", sans-serif; font-weight: 300;
    font-size: 11px; color: var(--white); line-height: 1; white-space: nowrap;
  }

  .emblem {
    position: absolute; border-radius: 50%; background: var(--white);
    display: flex; align-items: center; justify-content: center; text-align: center;
    font-family: "Josefin Sans", sans-serif; font-weight: 400; letter-spacing: 2px; text-transform: uppercase;
  }
  .label--riesling .emblem, .label--rose .emblem {
    left: 96px; top: 194px; width: 128px; height: 128px;
    border: 3px solid var(--accent); color: var(--accent); font-size: 13px; line-height: 1.5;
  }

  .origin {
    position: absolute; left: 0; width: 100%; text-align: center; white-space: nowrap;
    font-family: "Josefin Sans", sans-serif; font-weight: 300; letter-spacing: 0.5px; line-height: 1;
  }
  .label--riesling .origin, .label--rose .origin { top: 360px; font-size: 21px; color: var(--ink); }

  .facts {
    position: absolute; left: 0; width: 100%; display: flex; justify-content: center; gap: 26px;
    font-family: "Roboto Condensed", sans-serif; font-weight: 300; font-size: 13px; line-height: 1; white-space: nowrap;
  }
  .label--riesling .facts, .label--rose .facts { top: 420px; color: var(--accent); }

  /* Shiraz */
  .label--shiraz .ridge { top: 140px; bottom: 0; background: var(--shiraz-green); border-radius: 80px 120px 0 0; }
  .label--shiraz .emblem {
    left: 105px; top: 14px; width: 110px; height: 110px;
    border: 2px solid var(--shiraz-gold-light); color: var(--shiraz-green); font-size: 11px; line-height: 1.5;
  }
  .label--shiraz .title { top: 270px; font-size: 66px; letter-spacing: -1px; }
  .label--shiraz .stripe { border-color: var(--shiraz-gold-light); }
  .label--shiraz .band {
    top: 444px; height: 40px;
    background: linear-gradient(90deg, var(--shiraz-gold), var(--shiraz-gold-light) 50%, var(--shiraz-gold));
  }
  .label--shiraz .origin { top: 455px; font-size: 21px; color: var(--white); opacity: 0.85; }
  .label--shiraz .facts-vintage { top: 566px; color: var(--white); font-size: 13px; gap: 40px; }
  .label--shiraz .facts-volume { top: 600px; color: var(--shiraz-gold-light); font-size: 14px; }
</style>
</head>
<body>
<main class="lineup">

  <section class="label label--riesling" aria-label="Riesling label">
    <div class="ridge" role="img" aria-label="Mountain ridge silhouette in gold"></div>
    <div class="paper"></div>
    <h2 class="title">RIESLING</h2>
    <div class="stripe" style="top:220px"></div>
    <div class="band" style="top:244px;height:28px"></div>
    <span class="band-text" style="left:40px;top:253px">2022</span>
    <span class="band-text" style="right:26px;top:253px">NATURAL WINE</span>
    <div class="stripe" style="top:287px"></div>
    <div class="emblem">Kantina<br>e Drenit</div>
    <p class="origin">WINE OF ALBANIA</p>
    <p class="facts"><span>Vol 0.75l</span><span>Alc 14.3%,</span></p>
  </section>

  <section class="label label--rose" aria-label="Rose label">
    <div class="ridge" role="img" aria-label="Mountain ridge silhouette in pink"></div>
    <div class="paper"></div>
    <h2 class="title">ROSE</h2>
    <div class="stripe" style="top:220px"></div>
    <div class="band" style="top:244px;height:28px"></div>
    <span class="band-text" style="left:40px;top:253px">2022</span>
    <span class="band-text" style="right:26px;top:253px">NATURAL WINE</span>
    <div class="stripe" style="top:287px"></div>
    <div class="emblem">Kantina<br>e Drenit</div>
    <p class="origin">WINE OF ALBANIA</p>
    <p class="facts"><span>Vol 0.75l</span><span>Alc 14.3%,</span></p>
  </section>

  <section class="label label--shiraz" aria-label="Shiraz label">
    <div class="emblem">Kantina<br>e Drenit</div>
    <div class="ridge" role="img" aria-label="Mountain ridge silhouette in olive green"></div>
    <h2 class="title">SHIRAZ</h2>
    <div class="stripe" style="top:424px"></div>
    <div class="band"></div>
    <p class="origin">WINE OF ALBANIA</p>
    <div class="stripe" style="top:494px"></div>
    <p class="facts facts-vintage"><span>2020</span><span>NATURAL WINE</span></p>
    <p class="facts facts-volume"><span>Vol 0.75l</span><span>Alc 14.3%,</span></p>
  </section>

</main>
</body>
</html>
```